Business Website Re-design, Sharepoint, Office 365

Re-design of our existing Office 365 public website http://www.morrowvaltek.com. New site must use SharePoint and be compatible with Office 365 Hosting. A preliminary site layout and design is provided but creative suggestions and alternatives will be considered. Please see our attached power point presentation for details on the layout, and site design we are looking for.

Target Market(s)

Industrial Automation

Industry/Entity Type

Business

Coding

Coded - Design and coding required

Number of Pages Required

5+ page

Font styles to use
Serif
Sans Serif

Requirements
Must have
• SharePoint & Office 365 Compatible

```html
<!DOCTYPE html>
<html lang="en">
<head>
<meta charset="utf-8">
<title>Morrow Valtek</title>
<link rel="stylesheet" href="https://fonts.googleapis.com/css2?family=Open+Sans:wght@400;600;700&family=Lato:wght@400;700&display=swap">
<style>
  :root {
    --page-bg: #efefef;
    --panel: #ffffff;
    --brand: #c8401f;
    --brand-dark: #bf3b1d;
    --sidebar: #e0552c;
    --sidebar-active: #cc4523;
    --search: #c84724;
    --text: #444444;
    --text-soft: #666666;
    --rule: #dddddd;
    --quote: #d7d7d7;
  }
  * { margin: 0; padding: 0; box-sizing: border-box; }
  html, body { width: 1200px; height: 1154px; overflow: hidden; }
  body { background: var(--page-bg); font-family: "Open Sans", Arial, sans-serif; color: var(--text); position: relative; }
  .panel { position: absolute; left: 60px; top: 29px; width: 1080px; height: 1093px; background: var(--panel); }
  .abs { position: absolute; }

  .brand { left: 106px; top: 96px; display: flex; align-items: center; gap: 10px; }
  .brand-mark { width: 30px; height: 30px; border-radius: 50%; background: var(--brand); }
  .brand-name { font-size: 26px; font-weight: 700; color: var(--brand); letter-spacing: 1px; }

  .phone { left: 705px; top: 89px; display: flex; align-items: center; font-size: 17px; color: #333; white-space: nowrap; }
  .phone svg { margin-right: 10px; }
  .phone .phone-number { color: #555; margin-left: 5px; }
  .signin { left: 938px; top: 86px; width: 187px; height: 37px; background: var(--brand); color: #fff; font-size: 16px; display: flex; align-items: center; justify-content: center; letter-spacing: .3px; }

  .trail { left: 0; top: 0; }

  .sidebar { left: 74px; top: 210px; width: 270px; height: 429px; background: var(--sidebar); }
  .nav { list-style: none; }
  .nav li { height: 33.2px; display: flex; align-items: center; padding-left: 58px; position: relative; color: #fff; font-size: 14px; }
  .nav li::before { content: ""; position: absolute; left: 32px; width: 5px; height: 5px; border-radius: 50%; background: #fff; top: 12px; }
  .nav li.active { background: var(--sidebar-active); height: 35px; }
  .search { position: absolute; left: 30px; top: 361px; width: 215px; height: 34px; background: var(--search); display: flex; }
  .search span { flex: 1; color: #fff; font-size: 12px; padding: 10px 12px; }
  .search i { width: 30px; background: #b63c1e; display: flex; align-items: center; justify-content: center; }

  .hero { left: 375px; top: 210px; width: 751px; height: 314px; background: linear-gradient(180deg, #3a2a20 0%, #6b4320 40%, #c07a22 70%, #2b2320 100%); }
  .hero-arrow { position: absolute; top: 143px; width: 28px; height: 28px; border-radius: 50%; background: rgba(200,200,200,.7); display: flex; align-items: center; justify-content: center; }

  h2 { font-weight: 400; font-size: 22px; color: #333; letter-spacing: .2px; }
  .welcome { left: 374px; top: 545px; }
  .intro { left: 373px; top: 586px; width: 755px; font-size: 13px; line-height: 18.8px; color: var(--text-soft); }
  .more { left: 374px; top: 677px; width: 110px; height: 25px; background: var(--brand); color: #fff; font-size: 14px; display: flex; align-items: center; justify-content: center; }

  .testimonials { left: 374px; top: 742px; }
  .pager { top: 738px; width: 37px; height: 36px; border: 1px solid #e2e2e2; background: #f6f6f6; display: flex; align-items: center; justify-content: center; }
  .quote-mark { left: 374px; top: 812px; }
  .quote { left: 443px; top: 823px; width: 661px; font-size: 15.5px; line-height: 29px; color: #444; }
  .quote .line1 { display: block; border-bottom: 1px solid var(--rule); }
  .dots { left: 1059px; top: 893px; display: flex; gap: 6px; }
  .dots i { width: 4px; height: 4px; border-radius: 50%; background: var(--brand); }
  .person { right: 79px; top: 910px; text-align: right; font-family: Arial, sans-serif; }
  .person b { display: block; font-size: 14px; color: #222; }
  .person small { font-size: 12px; color: #888; }

  .footer { left: 60px; top: 1029px; width: 1080px; height: 93px; background: linear-gradient(180deg, #c9451f, #bd391b); color: #fff; }
  .footer-links { position: absolute; top: 15px; left: 0; width: 100%; text-align: center; font-size: 12px; }
  .footer-links span { margin: 0 8px; }
  .footer-rule { position: absolute; left: 12px; right: 12px; top: 48px; height: 1px; background: rgba(255,255,255,.25); }
  .copyright { position: absolute; left: 12px; top: 61px; font-family: Lato, Arial, sans-serif; font-size: 12.5px; }
  .social { position: absolute; right: 15px; top: 60px; display: flex; gap: 11px; }
  .social i { width: 19px; height: 19px; border-radius: 50%; background: #fff; }
</style>
</head>
<body>
  <div class="panel"></div>

  <div class="abs brand"><span class="brand-mark"></span><span class="brand-name">MORROW VALTEK</span></div>

  <div class="abs phone">
    <svg width="18" height="24" viewBox="0 0 18 24" aria-hidden="true"><path d="M5 1 L9 6 L6.5 9 Q8 14 11.5 17 L14.5 15 L17 20 L13 23 Q4 20 1.5 8 Q2 3 5 1 Z" fill="var(--brand)"/></svg>
    Toll Free:<span class="phone-number">1.800.555.0148</span>
  </div>
  <div class="abs signin">MORROW SIGNIN</div>

  <svg class="abs trail" width="1200" height="220" aria-hidden="true">
    <polyline points="343,210 363,161 381,189 598,189 618,169 842,182 881,166 937,183 1115,183" fill="none" stroke="var(--brand)" stroke-width="2.5"/>
    <polygon points="1113,176 1126,183 1113,190" fill="var(--brand)"/>
  </svg>

  <nav class="abs sidebar">
    <ul class="nav">
      <li class="active">Home</li>
      <li>Services</li>
      <li>Products</li>
      <li>Equipment</li>
      <li>News</li>
      <li>About us</li>
      <li>Contact us</li>
      <li>Remote Support</li>
      <li>Canadian Trackline</li>
      <li>USA Trackline</li>
    </ul>
    <div class="search">
      <span>Search Here</span>
      <i><svg width="12" height="12" viewBox="0 0 12 12" aria-hidden="true"><circle cx="5" cy="5" r="3.6" fill="none" stroke="#fff" stroke-width="1.4"/><line x1="7.6" y1="7.6" x2="11" y2="11" stroke="#fff" stroke-width="1.4"/></svg></i>
    </div>
  </nav>

  <div class="abs hero" role="img" aria-label="Night view of an illuminated oil and gas refinery with storage tanks and steam">
    <div class="hero-arrow" style="left:22px"><svg width="10" height="14" aria-hidden="true"><polyline points="8,1 2,7 8,13" fill="none" stroke="#fff" stroke-width="2"/></svg></div>
    <div class="hero-arrow" style="right:22px"><svg width="10" height="14" aria-hidden="true"><polyline points="2,1 8,7 2,13" fill="none" stroke="#fff" stroke-width="2"/></svg></div>
  </div>

  <h2 class="abs welcome">WELCOME TO OUR SITE</h2>
  <p class="abs intro">Morrow Valtek has been delivering proven results to our clients in the Oil and Gas industry through our line of process automation services since 2004. From consulting, to process control design, construction, programming,&nbsp; installation, maintenance and 24/7/365 service availability, we offer highly trained and certified personnel along with the latest advance­ments in controls and software to meet the clients specific needs or custom requirements.</p>
  <div class="abs more">Read More</div>

  <h2 class="abs testimonials">CUSTOMER TESTIMONIALS</h2>
  <div class="abs pager" style="left:1037px"><svg width="8" height="12" aria-hidden="true"><polyline points="2,1 6,6 2,11" fill="none" stroke="#888" stroke-width="1.3"/></svg></div>
  <div class="abs pager" style="left:1084px"><svg width="8" height="12" aria-hidden="true"><polyline points="2,1 6,6 2,11" fill="none" stroke="#888" stroke-width="1.3"/></svg></div>

  <svg class="abs quote-mark" width="52" height="38" viewBox="0 0 52 38" aria-hidden="true">
    <path d="M2 0 H20 V16 Q20 32 6 38 L4 34 Q11 28 11 20 H2 Z" fill="var(--quote)"/>
    <path d="M30 0 H48 V16 Q48 32 34 38 L32 34 Q39 28 39 20 H30 Z" fill="var(--quote)"/>
  </svg>
  <p class="abs quote"><span class="line1">Vitae adipiscing turpis. Aenean ligula nibh, molestie id viverra a, dapibus at dolor. In</span>iaculis viverra neque, ac eleifend ante lobortis id. In viverra ipsum ...</p>
  <div class="abs dots"><i></i><i></i><i></i></div>
  <div class="abs person"><b>Daniel Hartley</b><small>General Director</small></div>

  <footer class="abs footer">
    <div class="footer-links">Home<span>|</span>FAQ<span>|</span>Terms and Condition<span>|</span>Privacy Policy<span>|</span>Contact</div>
    <div class="footer-rule"></div>
    <div class="copyright">© 2015 Yoursite, All rights reserved.</div>
    <div class="social" aria-label="Social links"><i></i><i></i><i></i></div>
  </footer>
</body>
</html>
```